Charter Tour Boat Webpage Design

We need a web page design for a new business - Saltreef Tackle Tours, We do Fishing Charters, Montague Island Eco Tours, Diving, Whale Watching. We currently have a very basic website up. www.saltreeftackletours.example and as you can see we need a much better one.

Thanks!

Target Market(s)

Mainly fisherman, and families for tours

Industry/Entity Type

Business

Requirements
Must have
• page for fishing, montague island eco tours, whale watching.
Contact page, and enquiry page with form.

```html
<!DOCTYPE html>
<html lang="en">
<head>
<meta charset="utf-8">
<title>Saltreef Tackle Tours</title>
<link href="https://fonts.googleapis.com/css2?family=Source+Sans+3:wght@400;600&display=swap" rel="stylesheet">
<style>
:root{
  --sky-top:#7fd2f7;
  --sky-band:#3ea7df;
  --sky-low:#8bd6f6;
  --nav-top:#2a8ec0;
  --nav-bottom:#0b5d88;
  --nav-rule:#0a4c70;
  --panel:#ffffff;
  --rule:#dfe7ec;
  --heading:#e8582b;
  --text:#2b2b2b;
  --btn-top:#a6dcf8;
  --btn-bottom:#4aaee6;
  --btn-text:#0e4568;
  --footer-text:#1b3140;
}
*{box-sizing:border-box;margin:0;padding:0}
html,body{width:1029px;height:1200px;overflow:hidden}
body{
  position:relative;
  font-family:"Source Sans 3",sans-serif;
  color:var(--text);
  background:linear-gradient(180deg,var(--sky-top) 0,var(--sky-band) 118px,#5cbdea 122px,var(--sky-low) 420px,#7fd0f4 1200px);
}
.brand{position:absolute;left:116px;top:28px;display:flex;align-items:center;gap:8px}
.brand-dot{width:22px;height:22px;border-radius:50%;background:#0b5d88}
.brand-name{font-size:19px;font-weight:600;color:#0b4a70}
.main-nav{
  position:absolute;left:398px;top:39px;width:514px;height:35px;display:flex;
  border-radius:5px;overflow:hidden;
  background:linear-gradient(180deg,var(--nav-top),var(--nav-bottom));
  box-shadow:0 2px 3px rgba(0,0,0,.25);
}
.main-nav a{
  flex:auto;display:flex;align-items:center;justify-content:center;
  color:#fff;font-size:11px;text-decoration:none;border-left:1px solid var(--nav-rule);
}
.main-nav a:first-child{border-left:none}
.panel-wave{position:absolute;left:119px;top:100px;width:793px;height:60px}
.panel{
  position:absolute;left:119px;top:140px;width:793px;height:978px;background:var(--panel);
  border-radius:0 0 6px 6px;box-shadow:0 2px 6px rgba(0,40,80,.25);
}
.slider{
  position:absolute;left:132px;top:163px;width:766px;height:256px;border-radius:8px;
  background:linear-gradient(180deg,#c9d8e2 0,#9fb7c8 28%,#3f79a6 55%,#2b6896 100%);
  box-shadow:0 3px 5px rgba(0,0,0,.3);
}
.slider-arrow{
  position:absolute;top:100px;width:64px;height:34px;background:rgba(255,255,255,.25);
  display:flex;align-items:center;justify-content:center;
}
.slider-arrow.prev{left:0}
.slider-arrow.next{right:0}
h2{position:absolute;font-weight:400;font-size:21px;color:var(--heading)}
.card{
  position:absolute;left:138px;top:484px;width:439px;height:145px;border:1px solid #d8dde0;
  border-radius:8px;background:#fff;
}
.photo{position:absolute}
.copy{position:absolute;font-size:10.5px;line-height:17px;text-align:justify}
.btn{
  position:absolute;height:27px;border-radius:4px;display:flex;align-items:center;justify-content:center;
  font-size:11px;color:var(--btn-text);
  background:linear-gradient(180deg,var(--btn-top),var(--btn-bottom));
  box-shadow:0 2px 3px rgba(0,0,0,.25);
}
.contact-tab{
  position:absolute;left:607px;top:493px;width:34px;height:113px;border:1px solid #7cc9ee;border-radius:6px;
  background:linear-gradient(90deg,#e6f6fe,#b5e3f9);display:flex;align-items:center;justify-content:center;
}
.contact-tab span{transform:rotate(-90deg);white-space:nowrap;font-size:16px;color:#1f6e98}
.contact-card{
  position:absolute;left:641px;top:490px;width:248px;height:125px;border-radius:50% 0 0 50%/20%;
  background:#fff;box-shadow:0 6px 10px -4px rgba(0,0,0,.15);
}
.contact-line{position:absolute;left:27px;font-size:12px;color:#111}
.contact-icon{position:absolute;left:26px}
.contact-sep{position:absolute;left:55px;width:1px;height:20px;background:#ccc}
.rule{position:absolute;left:119px;width:793px;height:1px;background:var(--rule)}
.collage{position:absolute;left:145px;top:934px;width:205px;height:150px;background:#fff;padding:5px;
  box-shadow:0 2px 5px rgba(0,0,0,.35);transform:rotate(-1deg)}
.collage-back{position:absolute;left:150px;top:928px;width:200px;height:160px;background:#eee;
  box-shadow:0 1px 3px rgba(0,0,0,.3);transform:rotate(2deg)}
.collage .photo{position:static;width:100%;height:100%}
.follow{position:absolute;left:118px;top:1152px;font-size:13px;color:var(--footer-text)}
.social{position:absolute;top:1145px;width:27px;height:27px;border-radius:50%;
  background:radial-gradient(circle at 40% 35%,#fff,#d6eaf5);box-shadow:0 1px 2px rgba(0,0,0,.3)}
.footer-nav{position:absolute;right:122px;top:1141px;font-size:10px;color:var(--footer-text)}
.footer-nav a{color:var(--footer-text);text-decoration:none}
.footer-nav i{font-style:normal;margin:0 6px}
.legal{position:absolute;right:122px;top:1161px;font-size:10px;color:var(--footer-text)}
</style>
</head>
<body>
<div class="brand"><span class="brand-dot"></span><span class="brand-name">Saltreef Tackle Tours</span></div>

<nav class="main-nav">
  <a href="#">Home</a><a href="#">Fishing</a><a href="#">Montague Island</a><a href="#">Whale Watching</a><a href="#">Book Now</a><a href="#">Contact Us</a>
</nav>

<svg class="panel-wave" viewBox="0 0 793 60" preserveAspectRatio="none" aria-hidden="true">
  <path d="M0 60 V40 C220 0 520 0 793 45 V60 Z" fill="#ffffff"/>
  <path d="M0 40 C220 0 520 0 793 45" fill="none" stroke="#7fd2f7" stroke-width="3"/>
</svg>
<div class="panel"></div>

<div class="slider" role="img" aria-label="Photo of anglers holding their catch on a sport fishing boat at sea">
  <div class="slider-arrow prev"><svg width="10" height="14"><path d="M8 1 2 7l6 6" fill="none" stroke="#fff" stroke-width="2"/></svg></div>
  <div class="slider-arrow next"><svg width="10" height="14"><path d="M2 1l6 6-6 6" fill="none" stroke="#fff" stroke-width="2"/></svg></div>
</div>

<h2 style="left:144px;top:442px">Fishing</h2>
<div class="card"></div>
<div class="photo" role="img" aria-label="Photo of an angler holding a large fish on the ocean" style="left:158px;top:506px;width:110px;height:102px;background:linear-gradient(180deg,#8fc3e6,#2f6fa3);border-radius:3px"></div>
<p class="copy" style="left:286px;top:509px;width:241px">Targeting: Tuna, Marlin, Kingfish, Trumpeter, Blueeye Cod, Hapaku, Sharks and all our other local reef and deep water fish, depending on the season and charter and type of fishing you are interested in.</p>
<div class="btn" style="left:287px;top:587px;width:93px">Read More &gt;&gt;</div>

<div class="contact-card">
  <div class="contact-line" style="top:25px">PO Box 204, SALTREEF BAY&nbsp; NSW&nbsp; 2999</div>
  <svg class="contact-icon" style="top:57px" width="16" height="12" viewBox="0 0 16 12" aria-hidden="true"><rect x="0.5" y="0.5" width="15" height="11" fill="#9aa3a8"/><path d="M0.5 0.5 8 7l7.5-6.5" fill="none" stroke="#fff" stroke-width="1.4"/></svg>
  <div class="contact-sep" style="top:53px"></div>
  <div class="contact-line" style="top:53px;left:65px">rob@saltreeftackletours.example</div>
  <svg class="contact-icon" style="top:86px" width="16" height="16" viewBox="0 0 16 16" aria-hidden="true"><path d="M3 14c-2-3 0-9 6-11l2 3-2 1c-2 1-3 3-2 5l-2 2z" fill="#9aa3a8"/></svg>
  <div class="contact-sep" style="top:82px"></div>
  <div class="contact-line" style="top:82px;left:65px">0412 555 318</div>
</div>
<div class="contact-tab"><span>Contact Us</span></div>

<div class="rule" style="top:651px"></div>

<h2 style="left:139px;top:668px">Montague Island</h2>
<p class="copy" style="left:138px;top:703px;width:510px">Enjoy a 20 minture boat ride to Montague Island,&nbsp; keeping an eye out for Dolphin, whales and other wildlife, take a 1 hour guided tour of Montague Island, return to the boat for light refreshment, then cruise along the shore line, visiting the seal colonys, then enjoy your journey home.<br><br>Enjoy a 20 minture boat ride to the Island, keeping an eye out for dolphins, whales and other wildlife along the way, arriving at the island to vist the seal colonys, then a short cruise along the shore line, enjoying light refreshements, then&nbsp; take a 21/2 hour guided tour of the Island. Return to the boat for a cold drink and enjoy your journey home.</p>
<div class="photo" role="img" aria-label="Photo of seals resting on dark rocks by the sea" style="left:680px;top:704px;width:204px;height:117px;border-radius:5px;background:linear-gradient(180deg,#c7c3d6 0,#b9b4cb 35%,#5a4a36 55%,#3f5c90 75%,#2f5390 100%)"></div>
<div class="btn" style="left:135px;top:851px;width:94px">Read More &gt;&gt;</div>

<div class="rule" style="top:904px"></div>

<div class="collage-back"></div>
<div class="collage"><div class="photo" role="img" aria-label="Collage of fishing trip photos with anglers and their catch" style="background:linear-gradient(135deg,#b9d6e8,#2f6aa0 50%,#1f3f6e 70%,#9aa8b0)"></div></div>

<h2 style="left:373px;top:922px">Welcome to our site</h2>
<p class="copy" style="left:372px;top:960px;width:510px;line-height:19px">Rob Hartley has return from travelling and fishing Australia, to start Saltreef Tackle Tours. Previous manager/operator of Bluewater Run, Harbour Line Tours. We offer fully catered trips ranging from 2 to 9 hours weather fishing, diving, snorkeling, whale watching, Montague Island Eco Tour, or a mix of all our options. Specialising in small groups from shared charters to private with a personalised service. We use the latest top quality gear available from our fishing tackle, lures to electronics. Our boat is a 9.8 metre purpose built fishing and tour boat, with toilet and cooking facilities. We offer tea, coffee, soft drinks, water, light refreshments on all our charters/tours and lunch is provided on a full day fishing charter. Our website is currently under construction!</p>

<div class="follow">Follow Us</div>
<div class="social" style="left:190px"></div>
<div class="social" style="left:225px"></div>
<div class="social" style="left:258px"></div>
<div class="social" style="left:291px"></div>

<div class="footer-nav"><a href="#">Home</a><i>|</i><a href="#">Fishing</a><i>|</i><a href="#">Montague Island</a><i>|</i><a href="#">Whale Watching</a><i>|</i><a href="#">Book Now</a><i>|</i><a href="#">Contact Us</a></div>
<div class="legal">Copyrights @ 2012 All Rights Reserved</div>
</body>
</html>
```